Family Photography A5 Invitation to prospective clients

A restaurant will give me public space at their entrance to promote my family photography. I need an A5 vertical layout design for a card to 'invite' potential clients to call me. I am a portrait photographer in Perth, Western Australia. The A5 cards will be taken away by potential clients. They are encouraged to call the studio to register their interest with a view to having a very beautiful family portrait in the studio or on location. This will save the family $250 because the fee will be waived. Locations for photography can include a sunset at the famous Wendham Beach or parks in the Western Suburbs of Perth. Prefer Indesign work file so that I can change images for reprints later. Will be happy to give extra ongoing work to the successful designer on future projects. I'm happy to take positional images in the design and change them later.

Target Market(s)

Women mainly in the 30 to 45 years age group

Industry/Entity Type

Restaurant

Font styles to use
Sans Serif

Requirements
Must have
• Call to action and lively design that gets attention. Prefer to have some similarity with style of web site marlowimaging.com.au
Nice to have
• Prefer not to have the look of fake 'competitions' but rather an invitation to have a beautiful experience and with the opportunity to purchase a beautiful piece of art that celebrates their family. See word doc for previous idea with 'win a portrait...' Some of the words might be useful. More here... Brent Marlow’s photography hangs on thousands of walls in Perth’s homes. His family portraits are not so much photographs as works of art, each one perfect in its own way, a unique interplay of light, shade, colour and composition. They’re the ones that make people say more than just, ‘Oh, nice’. They make people linger and say, ‘Wow, amazing!’.
Should not have
• Avoid too much emphasis on cost. I am not competing on cost, but rather trying to inspire the potential client. See word doc for previous idea with 'win a portrait...' Some of the words might be useful.

```html
<!DOCTYPE html>
<html lang="en">
<head>
<meta charset="utf-8">
<title>Marlow Imaging – Family Portrait Invitation</title>
<link href="https://fonts.googleapis.com/css2?family=PT+Sans:wght@400;700&family=Oswald:wght@500;700&family=Roboto:wght@300;400;500&display=swap" rel="stylesheet">
<style>
  :root {
    --green: #6e8c4f;
    --green-text: #6b8a45;
    --ink: #1a1a1a;
    --grey: #5f5f5f;
    --line: #cfcfcf;
    --white: #ffffff;
  }
  * { margin: 0; padding: 0; box-sizing: border-box; }
  html, body { width: 846px; height: 1200px; overflow: hidden; background: var(--white); }
  .card { position: relative; width: 846px; height: 1200px; background: var(--white); font-family: "PT Sans", sans-serif; color: var(--ink); }
  .top-band { position: absolute; left: 0; top: 0; width: 846px; height: 33px; background: var(--green); }

  .brand { position: absolute; left: 80px; top: 78px; width: 240px; height: 175px; display: flex; align-items: center; gap: 14px; }
  .brand-mark { width: 46px; height: 46px; border: 3px solid var(--ink); border-radius: 50%; flex: none; }
  .brand-name { font-family: "PT Sans", sans-serif; font-weight: 700; font-size: 30px; line-height: 1.1; color: var(--ink); }

  .call-box { position: absolute; left: 458px; top: 90px; }

  .letter { position: absolute; left: 46px; top: 286px; width: 760px; font-size: 17px; line-height: 22px; }
  .letter p { margin-bottom: 11px; }

  .family-photo { position: absolute; left: 0; top: 830px; width: 437px; height: 370px;
    background: radial-gradient(circle at 52% 4%, #f6e9a0 0%, #e6b84a 18%, #a8772a 45%, #5a4320 80%, #3a2c17 100%); }

  .locations { position: absolute; left: 437px; top: 823px; width: 409px; }
  .locations h2 { font-family: "Roboto", sans-serif; font-weight: 400; font-size: 14.5px; letter-spacing: 0.3px; color: var(--green-text); text-align: center; padding-top: 2px; }
  .location-tiles { display: flex; gap: 22px; margin: 16px 0 0 29px; }
  .tile { width: 105px; height: 73px; border: 1px solid var(--line); border-radius: 6px; box-shadow: 0 2px 3px rgba(0,0,0,0.15); display: flex; flex-direction: column; align-items: center; justify-content: flex-end; padding-bottom: 5px; background: var(--white); }
  .tile svg { margin-bottom: 4px; }
  .tile span { font-family: "Roboto", sans-serif; font-size: 8.5px; font-weight: 500; color: var(--grey); letter-spacing: 0.3px; }

  .booking { position: absolute; left: 437px; top: 957px; width: 409px; height: 243px; background: var(--green); color: var(--white); text-align: center; padding-top: 20px; }
  .booking .lead { font-family: "Roboto", sans-serif; font-weight: 300; font-size: 17.5px; line-height: 23px; }
  .booking .phone { font-family: "Oswald", sans-serif; font-weight: 700; font-size: 25px; margin-top: 12px; }
  .booking .address { font-family: "PT Sans", sans-serif; font-size: 13.5px; line-height: 19px; margin-top: 10px; padding: 0 22px; }
  .booking .web { font-family: "PT Sans", sans-serif; font-weight: 700; font-size: 13.5px; margin-top: 12px; }
</style>
</head>
<body>
<div class="card">
  <div class="top-band"></div>

  <div class="brand">
    <div class="brand-mark"></div>
    <div class="brand-name">Marlow<br>Imaging</div>
  </div>

  <svg class="call-box" width="330" height="172" viewBox="0 0 330 172" aria-label="Call me now 0400 318 275">
    <rect x="87" y="3" width="40" height="12" rx="4" fill="#d6d6d6"/>
    <rect x="256" y="0" width="48" height="14" rx="3" fill="#6e8c4f"/>
    <rect x="2" y="12" width="324" height="156" rx="12" fill="#fff" stroke="#d2d2d2" stroke-width="2.5"/>
    <circle cx="79" cy="87" r="68" fill="#e6e6e6"/>
    <circle cx="79" cy="87" r="62" fill="#8d96a0" role="img" aria-label="Photographer riding a bicycle"/>
    <text x="250" y="57" text-anchor="middle" font-family="Roboto, sans-serif" font-size="30" fill="#5f5f5f">Call me</text>
    <text x="250" y="104" text-anchor="middle" font-family="Roboto, sans-serif" font-size="44" fill="#5f5f5f">NOW</text>
    <line x1="152" y1="114" x2="304" y2="114" stroke="#cfcfcf" stroke-width="1.5"/>
    <text x="228" y="145" text-anchor="middle" font-family="Oswald, sans-serif" font-weight="500" font-size="27" fill="#6b8a45">0400 318 275</text>
  </svg>

  <div class="letter">
    <p>Hello,</p>
    <p>Thank you for dining with us at Corvella Restaurant in North Wendham. We’d love to invite you and your family to enjoy a portrait session with a renowned Western Australian photographer.</p>
    <p>Brent Marlow’s photography hangs on thousands of walls in Perth’s homes. His family portraits are not so much photographs as works of art, each one perfect in its own way.</p>
    <p>Each portrait is a unique interplay of light, shade, colour and composition. They’re the ones that make people linger and say, ‘Wow, amazing!’ We’d love to create one for you.</p>
    <p>You’ll be asked to imagine your perfect backdrop. Will it be a sunset at Wendham Beach? A park full of beautiful flowers and greenery? Or perhaps you’d prefer a creative black and white studio session at our North Fremantle studio? The choice is yours.</p>
    <p>After your session, we’ll arrange a cinema experience to highlight the many ways of presenting your beautiful images. We guarantee that your images will reflect personality, humour and love. Like so many of our clients, you’ll probably return in future years because our work really does keep on giving.</p>
    <p>See yourself in a new light. Simply mention this card when you call Brent, and your session fee will be waived. How easy is that?</p>
    <p>We look forward to meeting your family,</p>
    <p>Brent Marlow</p>
    <p>Phone 6400 2718</p>
  </div>

  <div class="family-photo" role="img" aria-label="Two young brothers facing each other in golden sunset light among coastal dunes"></div>

  <section class="locations">
    <h2>PHOTO SESSIONS ON LOCATION</h2>
    <div class="location-tiles">
      <div class="tile">
        <svg width="54" height="40" viewBox="0 0 54 40" aria-hidden="true">
          <polygon points="27,2 2,22 8,22 8,39 46,39 46,22 52,22" fill="#222"/>
          <rect x="38" y="5" width="5" height="10" fill="#222"/>
          <rect x="22" y="26" width="9" height="13" fill="#fff"/>
          <rect x="12" y="25" width="6" height="6" fill="#fff"/>
          <rect x="36" y="25" width="6" height="6" fill="#fff"/>
        </svg>
        <span>HOME</span>
      </div>
      <div class="tile">
        <svg width="64" height="40" viewBox="0 0 64 40" aria-hidden="true">
          <polygon points="4,38 16,18 28,38" fill="#222"/>
          <polygon points="40,38 48,6 56,38" fill="#222"/>
          <polygon points="50,38 57,14 64,38" fill="#222"/>
          <polygon points="30,38 36,12 42,38" fill="#222"/>
        </svg>
        <span>PARK</span>
      </div>
      <div class="tile">
        <svg width="80" height="40" viewBox="0 0 80 40" aria-hidden="true">
          <path d="M2,38 C10,10 30,4 40,18 C32,14 26,22 32,30 C38,36 44,34 48,30 L48,38 Z" fill="#222"/>
          <path d="M50,20 q5,-5 10,0 t10,0 t10,0" fill="none" stroke="#555" stroke-width="2"/>
          <path d="M50,28 q5,-5 10,0 t10,0 t10,0" fill="none" stroke="#555" stroke-width="2"/>
        </svg>
        <span>OCEAN</span>
      </div>
    </div>
  </section>

  <section class="booking">
    <p class="lead">Book your family photography session<br>today!</p>
    <p class="phone">Call us on 0400 318 275.</p>
    <p class="address">Office Admin 17 Alder St. Swanbourne 6010. Studio<br>8 Tolley St. North Fremantle 6159</p>
    <p class="web">www.marlowimaging.com.au</p>
  </section>
</div>
</body>
</html>
```